Window Treatment specialists need business card design

We are moving into a new location and want to highlight our expertise and all we have to offer. We are now a Marlowe Tenney Gallery for customized window treatments. We also offer custom soft treatments i.e drapery, valances, cornices, upholstery, pillows, color design services, outdoor fabrics, and specialize in motorization of hard treatments.

Target Market(s)

Home Owners 30- 55 with annual income $150,000 and up

Industry/Entity Type

Home Improvement

Contact Information for Business Card

We want our location, name, email, website, phone number, fax, business logo, and Marlowe Tenney logo on the card. Anything else we are open to the design.

Font styles to use
Sans Serif

Requirements
Must have
• location, name, email, website, phone number, fax, business logo, and Marlowe Tenney logo on the card. Anything else we are open to the design.

```html
<!DOCTYPE html>
<html lang="en">
<head>
<meta charset="utf-8">
<title>Solace Interiors – Business Card</title>
<link href="https://fonts.googleapis.com/css2?family=Lato:wght@400;700;900&display=swap" rel="stylesheet">
<style>
  :root {
    --teal: #a3cbce;
    --teal-deep: #9cc7ca;
    --ink: #141414;
    --grey: #777777;
    --slate: #4f6670;
    --orange: #ef8a2c;
    --paper: #ffffff;
  }
  * { margin: 0; padding: 0; box-sizing: border-box; }
  html, body { width: 1200px; height: 720px; overflow: hidden; background: var(--paper); }
  body { font-family: "Lato", Arial, sans-serif; }

  .card { position: relative; width: 1200px; height: 720px; background: var(--paper); overflow: hidden; }

  .brand {
    position: absolute; left: 110px; top: 110px; width: 330px;
    text-align: center; color: var(--teal);
  }
  .brand-dot {
    display: block; width: 150px; height: 150px; margin: 0 auto 26px;
    border-radius: 50%; background: var(--teal);
  }
  .brand-name {
    font-weight: 400; font-size: 54px; line-height: 1.0; letter-spacing: 1px; color: var(--teal);
  }

  .divider {
    position: absolute; left: 492px; top: 48px; width: 5px; height: 428px;
    background: linear-gradient(to bottom, rgba(163,203,206,0) 0%, var(--teal) 40%, var(--teal) 60%, rgba(163,203,206,0) 100%);
  }

  .person { position: absolute; left: 551px; top: 70px; }
  .person-name { font-weight: 700; font-size: 38px; color: var(--teal-deep); line-height: 1.1; }
  .person-title { font-weight: 400; font-size: 27px; color: var(--grey); margin-top: 8px; }

  .contacts { position: absolute; left: 551px; top: 228px; list-style: none; }
  .contact { display: flex; align-items: flex-start; font-weight: 700; font-size: 28px; color: var(--ink); line-height: 40px; margin-bottom: 18px; }
  .contact-icon { width: 34px; height: 40px; margin-right: 18px; flex: none; }
  .contact-icon svg { width: 34px; height: 40px; display: block; }
  .contact-address { line-height: 40px; }

  .gallery {
    position: absolute; left: 0; right: 0; top: 528px; display: flex; justify-content: center; align-items: center;
  }
  .gallery-dot { width: 50px; height: 50px; border-radius: 50%; background: var(--orange); margin-right: 18px; }
  .gallery-name { font-weight: 700; font-size: 48px; color: var(--slate); letter-spacing: -0.5px; }

  .footer-band {
    position: absolute; left: 0; bottom: 0; width: 1200px; height: 98px; background: var(--teal);
    display: flex; align-items: center; justify-content: center;
  }
  .website { color: var(--paper); font-weight: 700; font-size: 31px; letter-spacing: 7px; }
</style>
</head>
<body>
<div class="card">

  <div class="brand">
    <span class="brand-dot"></span>
    <div class="brand-name">solace<br>interiors</div>
  </div>

  <div class="divider"></div>

  <div class="person">
    <div class="person-name">Daniel Ashcroft</div>
    <div class="person-title">President</div>
  </div>

  <ul class="contacts">
    <li class="contact">
      <span class="contact-icon">
        <svg viewBox="0 0 34 40" aria-hidden="true"><path fill="#a3cbce" d="M2 14c0-4 6-7 15-7s15 3 15 7v3h-7v-3c-2-1-5-1.5-8-1.5s-6 .5-8 1.5v3H2z"/><path fill="#a3cbce" d="M8 19h18l4 14H4z"/><g fill="#fff"><rect x="11" y="22" width="3" height="2.5"/><rect x="15.5" y="22" width="3" height="2.5"/><rect x="20" y="22" width="3" height="2.5"/><rect x="11" y="26" width="3" height="2.5"/><rect x="15.5" y="26" width="3" height="2.5"/><rect x="20" y="26" width="3" height="2.5"/></g></svg>
      </span>
      215.555.0148
    </li>
    <li class="contact">
      <span class="contact-icon">
        <svg viewBox="0 0 34 40" aria-hidden="true"><rect x="8" y="8" width="18" height="8" fill="#a3cbce"/><rect x="2" y="15" width="30" height="14" rx="3" fill="#a3cbce"/><rect x="9" y="24" width="16" height="10" fill="#fff" stroke="#a3cbce" stroke-width="2.5"/><circle cx="27" cy="19.5" r="1.6" fill="#fff"/></svg>
      </span>
      215.555.0163
    </li>
    <li class="contact">
      <span class="contact-icon">
        <svg viewBox="0 0 34 40" aria-hidden="true"><rect x="2" y="10" width="30" height="21" fill="#a3cbce"/><path d="M3 11l14 11 14-11M3 30l10-9M31 30l-10-9" fill="none" stroke="#fff" stroke-width="1.8"/></svg>
      </span>
      dashcroft@solaceinteriors.biz
    </li>
    <li class="contact">
      <span class="contact-icon">
        <svg viewBox="0 0 34 40" aria-hidden="true"><path fill="#a3cbce" d="M17 3c-6.5 0-11 4.8-11 10.8C6 21.5 17 34 17 34s11-12.5 11-20.2C28 7.8 23.5 3 17 3z"/><circle cx="17" cy="13.5" r="4.3" fill="#fff"/></svg>
      </span>
      <span class="contact-address">The Courtyard at Linden Row<br>412 Harrow Pike, Elm Grove, PA. 19077</span>
    </li>
  </ul>

  <div class="gallery">
    <span class="gallery-dot"></span>
    <span class="gallery-name">Marlowe Tenney Gallery</span>
  </div>

  <div class="footer-band">
    <span class="website">www.solaceinteriors.biz</span>
  </div>

</div>
</body>
</html>
```